Flyers

Modify Existing Flyer and create another for exterior company
Updates

Previous Brief has been updated- we want to update this existing one also

Target Market(s)

Exterior Remodeling Customers

Industry/Entity Type

Remodeling/Construction

```html
<!DOCTYPE html>
<html lang="en">
<head>
<meta charset="utf-8">
<title>Northvale Roofing and Exteriors – Remodeling Flyer</title>
<link href="https://fonts.googleapis.com/css2?family=Montserrat:wght@400;500;600;700;800&display=swap" rel="stylesheet">
<style>
  :root{
    --ink:#111111;
    --text:#2b2b2b;
    --orange:#e8542a;
    --blue:#1c6fbe;
    --paper:#ffffff;
    --stage:#ececec;
    --rule:#555555;
  }
  *{box-sizing:border-box;margin:0;padding:0}
  html,body{width:699px;height:1200px;overflow:hidden}
  body{background:var(--stage);font-family:'Montserrat',sans-serif;color:var(--text);position:relative}
  .flyer{position:absolute;left:0;top:147px;width:699px;height:905px;background:var(--paper);overflow:hidden;box-shadow:0 2px 8px rgba(0,0,0,.2)}
  .header{position:absolute;left:0;top:0;width:699px;height:123px;background:var(--ink)}
  .brand{position:absolute;left:46px;top:17px;width:206px;height:88px;display:flex;align-items:center;gap:8px;padding-left:10px}
  .brand-mark{width:14px;height:14px;background:var(--orange)}
  .brand-name{color:var(--paper);font-weight:600;font-size:13px;line-height:1.25;letter-spacing:.3px;text-transform:uppercase}
  .cta{position:absolute;left:492px;top:28px;color:var(--paper);font-weight:600;font-size:13px;line-height:1.2}
  .cta .free{color:var(--orange);font-weight:700}
  .cta .phone{display:block;font-size:27px;font-weight:700;margin-top:6px;letter-spacing:.2px}
  .rule-top{position:absolute;left:0;top:126px;width:699px;height:3px;background:var(--orange)}
  .intro{position:absolute;left:22px;top:150px;width:320px}
  .intro .lead{font-size:15.5px;font-weight:500;color:var(--text)}
  .intro .kitchen{font-size:23px;font-weight:800;color:var(--orange);margin-top:2px}
  .intro .or{font-size:15px;font-weight:500;color:var(--text)}
  .intro .bath{font-size:23px;font-weight:800;color:var(--blue);line-height:1.1}
  .intro .pitch{margin-top:34px;font-size:13px;font-weight:500;line-height:1.55;text-transform:uppercase}
  .intro .pitch strong{font-size:17px;font-weight:800}
  .intro .town{font-size:19.5px;font-weight:800;margin-top:4px;color:#222}
  .photo{position:absolute}
  .photo-kitchen{left:348px;top:133px;width:347px;height:228px;background:linear-gradient(160deg,#e4e4e2 0%,#cfcfcd 55%,#7a5a3e 100%)}
  .photo-bath{left:2px;top:363px;width:346px;height:226px;background:linear-gradient(120deg,#8a6a44 0%,#c9a26a 40%,#e2d6c8 75%,#f0ece6 100%)}
  .service{position:absolute;font-size:11.2px;line-height:1.22}
  .service h2{font-size:15.5px;font-weight:800;line-height:1.2;text-transform:uppercase}
  .service h2 .top{color:var(--blue);display:block}
  .service h2 .bottom{color:var(--orange);display:block}
  .service p{margin-top:4px}
  .service ul{list-style:none;margin-top:8px;padding-left:12px}
  .service li{line-height:1.42}
  .service li::before{content:"• "}
  .service .icon{position:absolute;stroke:var(--blue);fill:none;stroke-width:1.4}
  .svc-kitchen{left:393px;top:371px;width:290px}
  .svc-kitchen .icon{left:130px;top:0;width:40px;height:36px}
  .svc-bath{left:22px;top:618px;width:178px}
  .svc-bath .icon{left:140px;top:0;width:34px;height:36px}
  .svc-bath p{text-align:justify}
  .svc-home{left:259px;top:618px;width:180px}
  .svc-home .icon{left:134px;top:0;width:44px;height:36px}
  .svc-deck{left:500px;top:618px;width:178px}
  .svc-deck .icon{left:140px;top:0;width:36px;height:36px}
  .svc-deck p{text-align:justify}
  .divider{position:absolute;top:636px;width:1px;height:184px;background:var(--rule)}
  .d1{left:228px}.d2{left:470px}
  .rule-bottom{position:absolute;left:0;top:858px;width:699px;height:3px;background:var(--orange)}
  .footer{position:absolute;left:0;top:869px;width:699px;height:36px;background:var(--blue);color:var(--paper);font-weight:700;font-size:15px;display:flex;align-items:center;justify-content:center;letter-spacing:.5px}
</style>
</head>
<body>
<main class="flyer">
  <header class="header">
    <div class="brand">
      <span class="brand-mark"></span>
      <span class="brand-name">Northvale<br>Roofing and Exteriors</span>
    </div>
    <div class="cta">CALL TODAY FOR YOUR<br><span class="free">FREE</span> ESTIMATE<span class="phone">555-014-2287</span></div>
  </header>
  <div class="rule-top"></div>

  <section class="intro">
    <div class="lead">Ready for a Beautiful and Functional</div>
    <div><span class="kitchen">KITUCHEN</span> <span class="or">or</span></div>
    <div class="bath">BATHROOM?</div>
    <div class="pitch">Work with a <strong>TOP-RATED</strong> local<br>remodeling company in</div>
    <div class="town">ANKENY,AI</div>
  </section>

  <div class="photo photo-kitchen" role="img" aria-label="Modern white kitchen with island, bar stools and wood floor"></div>
  <div class="photo photo-bath" role="img" aria-label="Bathroom with marble double vanity, large mirror and soaking tub"></div>

  <section class="service svc-kitchen">
    <h2><span class="top">Kitichen</span><span class="bottom">Remodeling</span></h2>
    <svg class="icon" viewBox="0 0 40 36"><rect x="2" y="2" width="8" height="6"/><rect x="30" y="2" width="8" height="6"/><path d="M20 2v6M15 12h10l-2-4h-6z"/><rect x="2" y="20" width="36" height="14"/><path d="M2 24h36M14 24v10M26 24v10"/></svg>
    <p>Whatever your vision is for your new kitchen our crew can help you bring it to life. You can trust us for:</p>
    <ul>
      <li>Open concept design services</li>
      <li>Kitchen cabinet installation services</li>
      <li>Kitchen counter top installation services</li>
      <li>Tile installation services</li>
      <li>Plumbing upgrade services</li>
      <li>Electrical upgrade services</li>
      <li>Drywall services</li>
      <li>Painting services</li>
    </ul>
  </section>

  <section class="service svc-bath">
    <h2><span class="top">Bathroom</span><span class="bottom">Remodeling</span></h2>
    <svg class="icon" viewBox="0 0 34 36"><rect x="3" y="12" width="28" height="22"/><path d="M3 18h28M17 18v16M12 4h10v8M22 6h4"/></svg>
    <p>When you hire us for your bathroom remodeling project, the possibilities are endless. Our experienced and talented team can:</p>
    <ul>
      <li>Install a sutom tile shower</li>
      <li>Build a new vanity</li>
      <li>Install flooring and tile</li>
      <li>Replace your plumbing<br>&nbsp;&nbsp;and light fixtures</li>
    </ul>
  </section>
  <div class="divider d1"></div>

  <section class="service svc-home">
    <h2><span class="top">Home</span><span class="bottom">Additions</span></h2>
    <svg class="icon" viewBox="0 0 44 36"><path d="M4 12L22 3l18 9M6 12h32v20H6zM2 34h40"/><path d="M12 16v12M18 16v12M24 16v12M30 16v12"/></svg>
    <p>No matter what kind of space you need, our team will bring your vision to life. You can hire us if you need a:</p>
    <ul>
      <li>Bathroom addition</li>
      <li>Bedreoom addition</li>
      <li>Garage addition</li>
      <li>Basement addition</li>
      <li>Guest room addition</li>
      <li>Living room addition</li>
      <li>Sunroom addition</li>
    </ul>
  </section>
  <div class="divider d2"></div>

  <section class="service svc-deck">
    <h2><span class="top">Decks /</span><span class="bottom">Patios</span></h2>
    <svg class="icon" viewBox="0 0 36 36"><path d="M6 14a12 9 0 0 1 24 0zM18 14v14M4 26h28l-4 6M8 26l-4 6"/></svg>
    <p>An outdoor space is a great addition to any residential property. When you decide to build a patio or deck, you'll be able to experience a variety of benefits. Your outdoor area will increase your:</p>
    <ul>
      <li>Property value</li>
      <li>Curb appeal</li>
      <li>Functional living space</li>
    </ul>
  </section>

  <div class="rule-bottom"></div>
  <footer class="footer">www.northvaleexteriors.com</footer>
</main>
</body>
</html>
```